Meridel Haulage - Website

A clean, not cluttered informative website for our business. We specialize in the transportation of radioactive materials across North America. The site is mostly for information about our company and will not be used to attract business but will be used to attract employee's mainly drivers. Driver's are very hard to find in our area. One of the pages needs to be a job's posting page with an apply now button. Either an application can be filled out there or a resume can be uploaded which ever functionality works better. I would like a website that I can easily edit, ability to change text and photos.

Number of Pages Required

5+ page

Colors

Designer to choose colors to be used in the design.

Requirements
Must have
• Home - About - Services - Jobs - Contact pages
• A way prospective employee's can apply or upload their resume to be emailed to me
• Very clean apperance
Should not have
• I don't want it to be busy

```html
<!DOCTYPE html>
<html lang="en">
<head>
<meta charset="utf-8">
<title>Meridel Haulage</title>
<link href="https://fonts.googleapis.com/css2?family=Titillium+Web:wght@400;600;700&family=Raleway:wght@400;500;600&family=Open+Sans:ital,wght@0,400;0,600;1,400&display=swap" rel="stylesheet">
<style>
:root{
  --orange:#f7941d;
  --dark:#1f2226;
  --ink:#333;
  --muted:#666;
  --line:#dcdcdc;
  --light:#f8f8f8;
  --white:#fff;
}
*{margin:0;padding:0;box-sizing:border-box}
html,body{width:1200px;height:2423px;overflow:hidden}
body{position:relative;background:var(--white);font-family:"Open Sans",sans-serif;color:var(--ink)}
.abs{position:absolute}
.hero{left:0;top:0;width:1200px;height:610px;background:linear-gradient(180deg,#3a4048 0%,#2a3036 45%,#1e2427 100%)}
.logo{left:132px;top:28px;font-family:"Titillium Web",sans-serif;font-weight:700;font-size:34px;color:var(--orange);letter-spacing:1px;display:flex;align-items:center;gap:10px}
.logo .dot{width:14px;height:14px;border-radius:50%;background:var(--orange)}
.nav{top:36px;left:0;width:1200px;height:53px;border-bottom:1px solid rgba(255,255,255,.25)}
.nav a{position:absolute;top:3px;font-family:"Open Sans",sans-serif;font-size:16px;color:var(--white);text-decoration:none}
.nav a.active{color:var(--orange)}
.hero-title{top:190px;left:0;width:1200px;text-align:center;font-family:"Titillium Web",sans-serif;font-weight:600;font-size:50px;line-height:57px;color:var(--white)}
.hero-link{top:323px;left:0;width:1200px;text-align:center;font-style:italic;font-size:15px;color:#ccc}
.hero-link span{color:var(--orange);font-style:normal;margin-left:6px}
.trucks{left:258px;top:396px;width:711px;height:315px;background:radial-gradient(ellipse at 50% 45%,#f2c300 0%,#d8a800 45%,rgba(120,120,120,.6) 80%,rgba(200,200,200,0) 100%)}
h2{font-family:"Titillium Web",sans-serif;font-weight:600;font-size:29px;color:var(--orange);letter-spacing:.5px}
.p{font-size:12.5px;line-height:16px;color:var(--muted)}
.btn{display:flex;align-items:center;justify-content:center;background:var(--orange);color:var(--white);border-radius:20px;font-family:"Raleway",sans-serif;font-size:15px}
.map{left:380px;top:760px;width:300px;height:300px;background:radial-gradient(circle,#f0f0f0 0%,rgba(255,255,255,0) 70%)}
.grid{left:635px;top:766px;width:433px;height:277px;border:1px solid #e6e6e6;display:grid;grid-template-columns:1fr 1fr;grid-template-rows:1fr 1fr}
.cell{display:flex;flex-direction:column;align-items:center;justify-content:center;gap:14px;font-family:"Raleway",sans-serif;font-size:15.5px;color:var(--ink);border-right:1px solid #e6e6e6;border-bottom:1px solid #e6e6e6}
.cell.on{background:var(--orange);color:var(--white)}
.about-photo{left:0;top:1093px;width:601px;height:390px;background:linear-gradient(160deg,#5d8ec4 0%,#c9d7e4 40%,#e9ecef 60%,#7a7f83 100%)}
.about-bg{left:601px;top:1093px;width:599px;height:390px;background:linear-gradient(180deg,#232b38 0%,#1d2532 60%,#2c333b 100%)}
.about-bg .p{color:#e6e6e6}
.faq{left:132px;width:430px;border:1px solid var(--line);background:var(--white)}
.faq-head{height:40px;display:flex;align-items:center;justify-content:space-between;padding:0 24px;font-size:14.5px;color:var(--ink)}
.faq-head .ico{width:15px;height:15px;border-radius:50%;background:#111;color:#fff;font-size:13px;line-height:15px;text-align:center;font-weight:700}
.faq.open .faq-head{background:var(--orange);color:var(--white);height:44px}
.faq.open .ico{background:#fff;color:var(--orange)}
.faq-body{padding:20px 24px;font-size:12.5px;line-height:16px;color:var(--muted)}
.job{left:638px;width:430px;border:1px solid var(--line);padding:22px 25px;background:var(--white)}
.job h3{font-family:"Open Sans",sans-serif;font-weight:400;font-size:15px;color:#222;margin-bottom:8px}
.job .meta{display:flex;justify-content:space-between;margin-top:12px;font-size:14px;font-family:"Raleway",sans-serif}
.job .meta b{color:var(--orange);font-weight:600}
.join-dark{left:0;top:2010px;width:1200px;height:413px;background:linear-gradient(180deg,#262626,#1b1b1b)}
.join-title{left:132px;top:2018px;font-family:"Titillium Web",sans-serif;font-weight:700;font-size:36px;line-height:36px;color:var(--white)}
.join-sub{left:134px;top:2097px;font-size:13px;color:var(--white)}
.upload{left:601px;top:2045px;width:379px;height:56px;background:var(--white);padding:0 22px;display:flex;align-items:center;font-size:13px;color:#aaa}
.upload-btn{left:980px;top:2045px;width:88px;height:56px;background:var(--orange);display:flex;align-items:center;justify-content:center}
.foot-logo{left:136px;top:2198px;font-family:"Titillium Web",sans-serif;font-weight:700;font-size:32px;color:var(--white);letter-spacing:1px}
.foot-text{left:136px;top:2270px;width:300px;font-size:12.5px;line-height:15px;color:#ddd}
.vline{top:2168px;width:1px;height:210px;background:rgba(255,255,255,.2)}
.foot-h{font-family:"Titillium Web",sans-serif;font-weight:600;font-size:18px;color:var(--white)}
.contact-row{left:488px;display:flex;gap:22px;font-size:13px;line-height:16px;color:#eee}
.links{font-size:13px;line-height:19px;color:#ddd;list-style:none}
.socials{left:132px;top:2388px;display:flex;gap:6px}
.socials span{width:20px;height:20px;border:1.5px solid #ddd;border-radius:50%}
.copy{top:2393px;font-size:10.5px;color:var(--white)}
</style>
</head>
<body>

<section class="abs hero" role="img" aria-label="Mountain highway at dusk with a truck on the road"></section>
<div class="abs logo"><span class="dot"></span>MERIDEL HAULAGE</div>
<nav class="abs nav">
  <a class="active" style="left:556px">Home</a>
  <a style="left:644px">Services</a>
  <a style="left:749px">About Us</a>
  <a style="left:856px">Jobs</a>
  <a style="left:928px">Contact Us</a>
  <svg style="position:absolute;left:1048px;top:1px" width="20" height="20" viewBox="0 0 20 20" fill="none" stroke="#fff" stroke-width="2"><circle cx="8" cy="8" r="6"/><path d="M13 13l5 5"/></svg>
</nav>
<h1 class="abs hero-title">Strongest Distribution<br>Network.</h1>
<div class="abs hero-link">find out jobs<span>›</span></div>
<div class="abs trucks" role="img" aria-label="Three yellow semi trucks parked side by side"></div>

<div class="abs map" role="img" aria-label="Faint world map"></div>
<h2 class="abs" style="left:132px;top:786px">OUR SERVICES</h2>
<p class="abs p" style="left:132px;top:846px;width:425px">Lorem ipsum dolor sit amet, egestas at ornare integer ullamcorper, vel eu aliquam integer varius imperdiet, felis rhoncus, nulla congue et vel wisi mi in, sociis orci integer turpis purus non. Sapien bibendum fermentum non vivamus. Lectus tempus enim</p>
<p class="abs p" style="left:132px;top:921px;width:425px">Lorem ipsum dolor sit amet, egestas at ornare integer ullamcorper, vel eu aliquam integer varius imperdiet</p>
<div class="abs btn" style="left:132px;top:992px;width:151px;height:38px">Read More</div>

<div class="abs grid">
  <div class="cell on">
    <svg width="44" height="32" viewBox="0 0 44 32" fill="none" stroke="#fff" stroke-width="2"><rect x="2" y="4" width="26" height="18"/><path d="M28 10h8l6 7v5H28z"/><circle cx="10" cy="25" r="3.5"/><circle cx="34" cy="25" r="3.5"/><path d="M10 13l4 4 7-8"/></svg>
    Lorem ipsum dolor sit
  </div>
  <div class="cell" style="border-right:0">
    <svg width="32" height="32" viewBox="0 0 32 32" fill="none" stroke="#f7941d" stroke-width="1.8"><circle cx="16" cy="16" r="13"/><ellipse cx="16" cy="16" rx="6" ry="13"/><path d="M3 16h26M5 9h22M5 23h22"/></svg>
    Lorem ipsum dolor sit
  </div>
  <div class="cell" style="border-bottom:0">
    <svg width="30" height="34" viewBox="0 0 30 34" fill="none" stroke="#f7941d" stroke-width="1.8"><path d="M10 3h10l-3 6h-4z"/><path d="M12 9C4 13 2 30 15 31c13-1 11-18 3-22z"/><path d="M18 17c-1-2-6-2-6 1s6 2 6 5-5 3-6 1M15 14v13"/></svg>
    Lorem ipsum dolor sit
  </div>
  <div class="cell" style="border:0">
    <svg width="32" height="32" viewBox="0 0 32 32" fill="none" stroke="#f7941d" stroke-width="1.8"><circle cx="16" cy="16" r="5"/><path d="M16 3v5M16 24v5M3 16h5M24 16h5M6.8 6.8l3.5 3.5M21.7 21.7l3.5 3.5M6.8 25.2l3.5-3.5M21.7 10.3l3.5-3.5"/><circle cx="16" cy="16" r="10"/></svg>
    Lorem ipsum dolor sit
  </div>
</div>

<div class="abs about-photo" role="img" aria-label="Driver standing beside a white semi truck"></div>
<div class="abs about-bg" role="img" aria-label="Dim highway at night"></div>
<h2 class="abs" style="left:636px;top:1159px">ABOUT MERIDEL HAULAGE</h2>
<p class="abs p" style="left:638px;top:1224px;width:430px;color:#e6e6e6">Lorem ipsum dolor sit amet, egestas at ornare integer ullamcorper, vel eu aliquam integer varius imperdiet, felis rhoncus, nulla congue et vel wisi mi in, sociis orci integer turpis purus non. Sapien bibendum fermentum non vivamus. Lectus tempus enim, dolores nunc. Lacinia dapibus, mi eget ultrices. Etiam erat aliquam sodales quis, dignissim sollicitudin nec, nisl eu orci a vitae sed lacus. Curabitur velit donec varius imperdiet amet metus, ut vestibulum, maecenas erat.</p>
<div class="abs btn" style="left:638px;top:1376px;width:149px;height:39px">Read More</div>

<div class="abs" style="left:0;top:1483px;width:1200px;height:507px;background:var(--light)"></div>
<h2 class="abs" style="left:132px;top:1530px">QUESTIONS (FAQS)</h2>
<h2 class="abs" style="left:636px;top:1530px">JOBS &amp; CAREERS</h2>

<div class="abs faq open" style="top:1602px">
  <div class="faq-head">Lorem ipsum dolor sit amet<span class="ico">−</span></div>
  <div class="faq-body">Lorem ipsum dolor sit amet, consectetur adipiscing elit, sed do eiusmod tempor incididunt ut labore et dolore magna aliqua. Lorem ipsum dolor sit amet, consectetur adipiscing elit, sed do</div>
</div>
<div class="abs faq" style="top:1767px"><div class="faq-head">Lorem ipsum dolor sit amet<span class="ico">+</span></div></div>
<div class="abs faq" style="top:1827px"><div class="faq-head">Lorem ipsum dolor sit amet<span class="ico">+</span></div></div>
<div class="abs faq" style="top:1887px"><div class="faq-head">Lorem ipsum dolor sit amet<span class="ico">+</span></div></div>

<div class="abs job" style="top:1604px;height:162px">
  <h3>Lorem ipsum dolor sit amet</h3>
  <p class="p">Lorem ipsum dolor sit amet, consectetur adipiscing elit, sed do eiusmod tempor incididunt ut labore et dolore magna aliqua. Lorem ipsum dolor sit amet, consectetur adipiscing elit, sed do</p>
  <div class="meta"><span><b>Posted on :</b> 09 Jan 2019</span><b>Apply For This Job</b></div>
</div>
<div class="abs job" style="top:1765px;height:165px">
  <h3>Lorem ipsum dolor sit amet</h3>
  <p class="p">Lorem ipsum dolor sit amet, consectetur adipiscing elit, sed do eiusmod tempor incididunt ut labore et dolore magna aliqua. Lorem ipsum dolor sit amet, consectetur adipiscing elit, sed do</p>
  <div class="meta"><span><b>Posted on :</b> 08 Dec 2018</span><b>Apply For This Job</b></div>
</div>

<div class="abs join-dark" role="img" aria-label="Darkened photo of trucks in a yard"></div>
<svg class="abs" style="left:0;top:1990px" width="570" height="152" viewBox="0 0 570 152"><polygon points="0,0 440,0 565,152 0,152" fill="#f7941d"/></svg>
<div class="abs join-title">WANT TO JOIN<br>OUR TEAM?</div>
<div class="abs join-sub">Drop Your Resume Here !</div>
<div class="abs upload">Upload your resume here</div>
<div class="abs upload-btn"><svg width="24" height="26" viewBox="0 0 24 26" fill="#fff"><polygon points="12,2 22,13 15,13 15,20 9,20 9,13 2,13"/><rect x="2" y="22" width="20" height="3"/></svg></div>

<div class="abs foot-logo">MERIDEL HAULAGE</div>
<p class="abs foot-text">Lorem ipsum dolor sit amet, consectetur adipiscing elit, sed do eiusmod tempor incididunt ut labore et dolore magnaaliqua.ed do eiusmod tempor incididunt ut labore et dolore magnaaliqua.</p>
<div class="abs socials"><span></span><span></span><span></span><span></span></div>
<div class="abs vline" style="left:449px"></div>
<div class="abs vline" style="left:759px"></div>

<div class="abs foot-h" style="left:488px;top:2186px">CONTACT US</div>
<div class="abs contact-row" style="top:2232px">
  <svg width="18" height="20" viewBox="0 0 18 20" fill="none" stroke="#ddd" stroke-width="1.5"><path d="M9 18s6-6 6-10a6 6 0 0 0-12 0c0 4 6 10 6 10z"/><circle cx="9" cy="8" r="2"/></svg>
  <span>2215 Larkspur Road, Unit 4<br>Fenwick Falls</span>
</div>
<div class="abs contact-row" style="top:2279px">
  <svg width="18" height="20" viewBox="0 0 18 20" fill="none" stroke="#ddd" stroke-width="1.5"><path d="M4 2l3 4-2 2c1 3 3 5 6 6l2-2 4 3-2 3C8 18 1 11 2 4z"/></svg>
  <span>0400-5550181<br>0400-5550192</span>
</div>
<div class="abs contact-row" style="top:2322px">
  <svg width="18" height="18" viewBox="0 0 18 18" fill="none" stroke="#ddd" stroke-width="1.5"><path d="M2 9l14-7-4 14-3-5z"/><path d="M9 11l7-9"/></svg>
  <span>hiring@meridelhaulage.com</span>
</div>

<div class="abs foot-h" style="left:806px;top:2186px">USEFUL LINKS</div>
<ul class="abs links" style="left:808px;top:2227px">
  <li>Tracking</li><li>FAQ's</li><li>Company News</li><li>Who We Are?</li><li>Our History</li><li>Customer Care</li>
</ul>
<ul class="abs links" style="left:958px;top:2227px">
  <li>All Services</li><li>Air Freight</li><li>Ocean Freight</li><li>Road &amp; Rail Freight</li><li>Warehousing</li>
</ul>

<svg class="abs" style="left:540px;top:2381px" width="660" height="42" viewBox="0 0 660 42"><polygon points="40,0 660,0 660,42 0,42" fill="#f7941d"/></svg>
<div class="abs copy" style="left:627px">All Rights Reserved © 2019 Meridel Haulage</div>
<div class="abs copy" style="left:895px">Terms &amp; Conditions &nbsp;|&nbsp; Privacy Policy</div>

</body>
</html>
```